Dr Peter Vandell
Urologist
Professional
Dr Peter Vandell MB,ChB(UCT), FC Urol.(SA)
Ridgeway Medicentre and Lanford Private Hospital PO Box 58147 Brookvale 4105
povandell@medinet-mail.co.za
Pr No 7315824
Please email me for scanned copies of the existing stationery and cards to see current format

```html
<!DOCTYPE html>
<html lang="en">
<head>
<meta charset="utf-8">
<title>Dr Peter Vandell – Stationery Set</title>
<link rel="stylesheet" href="https://fonts.googleapis.com/css2?family=Tinos:wght@400;700&display=swap">
<style>
:root{
  --stage:#e9e7e3;
  --paper:#ffffff;
  --brand-red:#9b1b24;
  --brand-red-deep:#8a1620;
  --ink:#1a1a1a;
  --muted:#7a7a7a;
  --rule:#cfcfcf;
  --flap-line:#dcdcdc;
}
*{box-sizing:border-box;margin:0;padding:0}
html,body{width:1200px;height:678px;overflow:hidden}
body{background:var(--stage);font-family:'Tinos',serif;color:var(--ink);position:relative}
.sheet{position:absolute;background:var(--paper);box-shadow:0 2px 6px rgba(0,0,0,.18);overflow:hidden}
.brand-band{position:absolute;left:0;bottom:0;width:100%;background:linear-gradient(to bottom,var(--brand-red),var(--brand-red-deep))}
.identity .name{color:var(--brand-red);font-weight:700;line-height:1.1;white-space:nowrap}
.identity .quals{color:var(--muted);letter-spacing:.04em;text-transform:uppercase;line-height:1.3;white-space:nowrap}
.identity .specialty{color:var(--brand-red);font-weight:700;line-height:1.2}
.contact{color:var(--muted);line-height:1.35;white-space:nowrap}
.footer-note{position:absolute;color:#fff;white-space:nowrap;z-index:1}

/* Business card */
.business-card{left:53px;top:307px;width:194px;height:120px}
.business-card .identity{text-align:center;padding-top:9px}
.business-card .name{font-size:12px}
.business-card .quals{font-size:5px}
.business-card .specialty{font-size:10px;margin-top:1px}
.business-card .contact-row{display:flex;justify-content:space-between;padding:7px 14px 0;font-size:4.6px}
.business-card .contact-row .col + .col{border-left:1px solid var(--rule);padding-left:6px}
.business-card .brand-band{height:16px}

/* Letterhead */
.letterhead{left:264px;top:36px;width:343px;height:595px}
.letterhead .header{display:flex;padding:22px 0 0 22px}
.letterhead .identity{padding-right:10px}
.letterhead .name{font-size:13px}
.letterhead .quals{font-size:5px}
.letterhead .specialty{font-size:12px;margin-top:8px}
.letterhead .contact{border-left:1px solid var(--rule);padding-left:8px;font-size:5px}
.letterhead .contact .practice{color:var(--ink);margin-bottom:6px}
.letterhead .brand-band{height:40px}
.letterhead .footer-note{right:20px;bottom:12px;font-size:5.5px}

/* Compliment slip */
.compliment-slip{left:689px;top:103px;width:468px;height:250px}
.compliment-slip .header{display:flex;padding:16px 0 0 24px}
.compliment-slip .identity{padding-right:12px}
.compliment-slip .name{font-size:15px}
.compliment-slip .quals{font-size:5.5px}
.compliment-slip .specialty{font-size:13px;margin-top:8px}
.compliment-slip .contact{border-left:1px solid var(--rule);padding-left:9px;font-size:5.5px;display:flex;gap:18px}
.compliment-slip .contact .practice{color:var(--ink)}
.compliment-slip .brand-band{height:42px}
.compliment-slip .footer-note{right:26px;bottom:14px;font-size:6px}

/* Envelope */
.envelope{position:absolute;left:689px;top:372px;width:468px;height:257px;box-shadow:0 2px 6px rgba(0,0,0,.18)}
.envelope svg{position:absolute;inset:0;width:100%;height:100%}
.envelope .flap-mark{position:absolute;left:0;right:0;top:30px;text-align:center}
.envelope .body-mark{position:absolute;left:0;right:0;top:170px;text-align:center}
.envelope .name{font-size:14px}
.envelope .flap-mark .name{color:#fff}
.envelope .flap-mark .quals{color:#f1d7d9}
.envelope .quals{font-size:5px}
</style>
</head>
<body>

<section class="sheet business-card" aria-label="Business card">
  <div class="identity">
    <div class="name">Dr Peter Vandell</div>
    <div class="quals">MB,ChB(UCT), FC Urol.(SA)</div>
    <div class="specialty">Urologist</div>
  </div>
  <div class="contact-row contact">
    <div class="col">Ridgeway Medicentre<br>Lanford Private Hospital<br>Tel 033 555 0182<br>Fax 033 555 0183</div>
    <div class="col">PO Box 58147<br>Brookvale 4105<br>povandell@medinet-mail.co.za<br>Emergencies 082 555 0147</div>
  </div>
  <div class="brand-band" role="img" aria-label="Red curved brand band with grey and black accent lines"></div>
</section>

<section class="sheet letterhead" aria-label="Letterhead">
  <div class="header">
    <div class="identity">
      <div class="name">Dr Peter Vandell</div>
      <div class="quals">MB,ChB(UCT), FC Urol.(SA)</div>
      <div class="specialty">Urologist</div>
    </div>
    <div class="contact">
      <div class="practice">Ridgeway Medicentre<br>and Lanford Private Hospital<br>Pr No 7315824</div>
      PO Box 58147<br>Brookvale 4105<br>Tel 033 555 0182<br>Fax 033 555 0183<br>povandell@medinet-mail.co.za
    </div>
  </div>
  <div class="brand-band" role="img" aria-label="Red curved brand band with grey and black accent lines"></div>
  <div class="footer-note">Emergencies 082 555 0147</div>
</section>

<section class="sheet compliment-slip" aria-label="Compliment slip">
  <div class="header">
    <div class="identity">
      <div class="name">Dr Peter Vandell</div>
      <div class="quals">MB,ChB(UCT), FC Urol.(SA)</div>
      <div class="specialty">Urologist</div>
    </div>
    <div class="contact">
      <div class="practice">Ridgeway Medicentre<br>and Lanford Private Hospital<br>Pr No 7315824</div>
      <div>PO Box 58147<br>Brookvale 4105<br>Tel 033 555 0182<br>Fax 033 555 0183<br>povandell@medinet-mail.co.za</div>
    </div>
  </div>
  <div class="brand-band" role="img" aria-label="Red curved brand band with grey and black accent lines"></div>
  <div class="footer-note">Emergencies 082 555 0147</div>
</section>

<section class="envelope" aria-label="Envelope">
  <svg viewBox="0 0 468 257" preserveAspectRatio="none">
    <rect x="0" y="0" width="468" height="257" fill="var(--paper)"/>
    <path d="M0 92 L234 200 L468 92" fill="none" stroke="var(--flap-line)" stroke-width="1.2"/>
    <path d="M0 257 L200 150 M468 257 L268 150" stroke="var(--flap-line)" stroke-width="1"/>
    <path d="M20 0 L448 0 L468 92 L0 92 Z" fill="var(--brand-red)"/>
  </svg>
  <div class="flap-mark identity">
    <div class="name">Dr Peter Vandell</div>
    <div class="quals">MB,ChB(UCT), FC Urol.(SA)</div>
  </div>
  <div class="body-mark identity">
    <div class="name">Dr Peter Vandell</div>
    <div class="quals">MB,ChB(UCT), FC Urol.(SA)</div>
  </div>
</section>

</body>
</html>
```